Boutique Film/TV Company needs Business Card Design

Please see our website for background on our company and look of our current logo: www.lumarocpictures.ca

Pantone 314U is our main colour.

Target Market(s)

Network of peers, funders and broadcasters.

Industry/Entity Type

Business

Requirements
Must have
• We would like rounded corners and the height of the card to be shorter than traditional (maybe?!)

It's important that we have room for our office address, office number, cell number, email address, website, facebook and linked-in info (though not all of us have a linked-in account).

Would like the logo to keep the exclamation marks over the letters but the tag line/tag words of "film - television - interactive" can stay or go or... surprise me!

Nice to have
• Silky matte finish.

We are open to a change in the font of our logo/name.

```html
<!DOCTYPE html>
<html lang="en">
<head>
<meta charset="utf-8">
<title>Lumaroc Business Card</title>
<link rel="stylesheet" href="https://fonts.googleapis.com/css2?family=Exo+2:ital,wght@0,300;0,400;0,500;1,400&display=swap">
<style>
  :root {
    --backdrop: #b4b4b4;
    --card-black: #000000;
    --brand-blue: #0b98cc;
    --brand-navy: #2a3b52;
    --logo-top: #0a82b4;
    --logo-bottom: #0e5f8c;
    --name-accent: #14a9e6;
    --text-light: #ffffff;
    --icon-blue: #1597d4;
  }
  * { margin: 0; padding: 0; box-sizing: border-box; }
  html, body { width: 1200px; height: 1000px; overflow: hidden; }
  body {
    position: relative;
    background: var(--backdrop);
    font-family: "Exo 2", sans-serif;
    color: var(--text-light);
  }
  .card {
    position: absolute;
    width: 754px;
    height: 427px;
    background: var(--card-black);
    border-radius: 9px;
    overflow: hidden;
  }
  .card--front { left: 39px; top: 40px; }
  .card--back { left: 384px; top: 517px; }
  .card__waves { position: absolute; inset: 0; width: 100%; height: 100%; }
  .logo-box {
    position: absolute;
    width: 256px;
    height: 133px;
    background: linear-gradient(180deg, var(--logo-top), var(--logo-bottom));
    display: flex;
    align-items: center;
    justify-content: center;
  }
  .card--front .logo-box { left: 0; top: 150px; border-radius: 0 3px 3px 0; }
  .card--back .logo-box { left: 262px; top: 158px; border-radius: 3px; }
  .logo-box__name {
    font-family: "Exo 2", sans-serif;
    font-weight: 400;
    font-size: 46px;
    color: var(--text-light);
    letter-spacing: 0.5px;
  }
  .identity {
    position: absolute;
    right: 45px;
    top: 130px;
    text-align: right;
  }
  .identity__name {
    font-weight: 300;
    font-size: 35px;
    letter-spacing: 2.5px;
    line-height: 1;
  }
  .identity__name .surname { color: var(--name-accent); }
  .identity__title {
    font-style: italic;
    font-weight: 400;
    font-size: 14px;
    letter-spacing: 0.8px;
    margin-top: 2px;
  }
  .contact-list {
    position: absolute;
    right: 40px;
    top: 215px;
    list-style: none;
    font-size: 13px;
    font-weight: 500;
    letter-spacing: 0.6px;
    text-align: right;
  }
  .contact-list li {
    display: flex;
    justify-content: flex-end;
    align-items: center;
    gap: 7px;
    margin-bottom: 8px;
    line-height: 1.15;
  }
  .contact-list .email { font-size: 14px; }
  .contact-icon { width: 18px; height: 18px; flex: none; }
</style>
</head>
<body>

  <section class="card card--front" aria-label="Card front">
    <svg class="card__waves" viewBox="0 0 754 427" preserveAspectRatio="none" aria-hidden="true">
      <path fill="var(--brand-blue)" d="M0,105 C150,250 450,390 754,364 L754,427 L0,427 Z"/>
      <path fill="var(--brand-navy)" d="M0,278 C180,370 430,430 754,364 L754,427 L0,427 Z"/>
    </svg>

    <div class="logo-box"><span class="logo-box__name">Lumaroc</span></div>

    <div class="identity">
      <h1 class="identity__name">Marcus<span class="surname">Hale</span></h1>
      <p class="identity__title">Executive Manager</p>
    </div>

    <ul class="contact-list">
      <li>
        <span>48 Brennan Street West, Suite 210<br>Toronto, Ontario M5V 2K4</span>
        <svg class="contact-icon" viewBox="0 0 18 18" aria-hidden="true"><path fill="var(--icon-blue)" d="M9 1a6 6 0 0 0-6 6c0 4.5 6 10 6 10s6-5.5 6-10a6 6 0 0 0-6-6zm0 8.3a2.3 2.3 0 1 1 0-4.6 2.3 2.3 0 0 1 0 4.6z"/></svg>
      </li>
      <li>
        <span class="email">marcushale@lumaroc.com</span>
        <svg class="contact-icon" viewBox="0 0 18 18" aria-hidden="true"><g fill="none" stroke="var(--icon-blue)" stroke-width="1.2"><rect x="1.5" y="4" width="15" height="10"/><path d="M1.5 4 9 10l7.5-6M1.5 14 7 9m9.5 5L11 9"/></g></svg>
      </li>
      <li>
        <span>416 555 0142</span>
        <svg class="contact-icon" viewBox="0 0 18 18" aria-hidden="true"><g fill="none" stroke="var(--icon-blue)" stroke-width="1.2"><rect x="5.5" y="2" width="7" height="14" rx="1"/><rect x="7" y="4" width="4" height="4"/><path d="M7 10.5h4M7 12.5h4"/></g></svg>
      </li>
      <li>
        <span>www.lumarocpictures.ca</span>
        <svg class="contact-icon" viewBox="0 0 18 18" aria-hidden="true"><g fill="none" stroke="var(--icon-blue)" stroke-width="1.1"><circle cx="9" cy="9" r="7"/><ellipse cx="9" cy="9" rx="3" ry="7"/><path d="M2 9h14M3 5.5h12M3 12.5h12"/></g></svg>
      </li>
    </ul>
  </section>

  <section class="card card--back" aria-label="Card back">
    <svg class="card__waves" viewBox="0 0 754 427" preserveAspectRatio="none" aria-hidden="true">
      <path fill="var(--brand-blue)" d="M331,0 C520,30 680,140 754,260 L754,0 Z"/>
      <path fill="var(--brand-navy)" d="M450,0 C590,30 690,90 754,152 L754,0 Z"/>
    </svg>
    <div class="logo-box"><span class="logo-box__name">Lumaroc</span></div>
  </section>

</body>
</html>
```